CareLumen business cards

We need a business card design that we could customize as needed for employees. We will need space for Name, Title, 1-2 phone numbers and email address.

We are a Pharmacy Benefits Management (PBM) company for hospice agencies and beginning a nationwide expansion. Attached is a vector file of our logo.

Cards can be single or double sided.

```html
<!DOCTYPE html>
<html lang="en">
<head>
<meta charset="utf-8">
<title>CareLumen business cards</title>
<link rel="stylesheet" href="https://fonts.googleapis.com/css2?family=Lato:wght@400;700&display=swap">
<style>
  :root {
    --bg: #e2e2e2;
    --brand-blue: #336789;
    --brand-green: #7d9b54;
    --ink: #3a3a3a;
    --rule: #c9c9c9;
    --paper: #ffffff;
  }
  * { margin: 0; padding: 0; box-sizing: border-box; }
  html, body {
    width: 1200px;
    height: 920px;
    overflow: hidden;
  }
  body {
    background: var(--bg);
    position: relative;
    font-family: "Lato", sans-serif;
  }
  .card {
    position: absolute;
    overflow: hidden;
  }
  .card--front {
    left: 98px;
    top: 90px;
    width: 613px;
    height: 349px;
    background: var(--brand-blue);
  }
  .card--back {
    left: 498px;
    top: 488px;
    width: 610px;
    height: 350px;
    background: var(--paper);
  }
  .brand {
    position: absolute;
    display: flex;
    align-items: center;
  }
  .brand__square {
    display: block;
    flex: none;
  }
  .brand__name {
    font-weight: 400;
    line-height: 1;
    letter-spacing: -0.5px;
  }
  .card--front .brand {
    left: 102px;
    top: 140px;
    gap: 16px;
  }
  .card--front .brand__square {
    width: 66px;
    height: 66px;
    background: var(--paper);
  }
  .card--front .brand__name {
    font-size: 56px;
    color: var(--paper);
  }
  .card--back .brand {
    left: 37px;
    top: 158px;
    gap: 10px;
  }
  .card--back .brand__square {
    width: 44px;
    height: 44px;
    background: var(--brand-blue);
  }
  .card--back .brand__name {
    font-size: 38px;
    color: var(--brand-green);
  }
  .divider {
    position: absolute;
    left: 330px;
    top: 116px;
    width: 1px;
    height: 128px;
    background: var(--rule);
  }
  .person {
    position: absolute;
    left: 350px;
    top: 122px;
  }
  .person__name {
    font-size: 18px;
    font-weight: 700;
    color: var(--brand-blue);
    line-height: 22px;
  }
  .person__title {
    font-size: 14px;
    color: var(--brand-green);
    line-height: 18px;
  }
  .contact {
    position: absolute;
    left: 350px;
    top: 180px;
    list-style: none;
  }
  .contact__item {
    display: flex;
    align-items: center;
    gap: 12px;
    height: 19px;
    font-size: 13px;
    color: var(--ink);
  }
  .contact__icon {
    width: 12px;
    height: 12px;
    flex: none;
    fill: var(--brand-green);
  }
  .wave {
    position: absolute;
    left: 0;
    bottom: 0;
    width: 610px;
    height: 40px;
  }
</style>
</head>
<body>

  <section class="card card--front" aria-label="Card front">
    <div class="brand">
      <span class="brand__square"></span>
      <span class="brand__name">CareLumen</span>
    </div>
  </section>

  <section class="card card--back" aria-label="Card back">
    <div class="brand">
      <span class="brand__square"></span>
      <span class="brand__name">CareLumen</span>
    </div>

    <div class="divider"></div>

    <div class="person">
      <p class="person__name">Mara Ellison</p>
      <p class="person__title">CareLumen</p>
    </div>

    <ul class="contact">
      <li class="contact__item">
        <svg class="contact__icon" viewBox="0 0 12 12" aria-hidden="true"><path d="M2.4 1 4.3 2.9 3.4 4.3c.7 1.7 2.2 3.2 3.9 3.9l1.4-.9L10.6 9.2 9.4 11C5 10.5 1.5 7 1 2.6Z"/></svg>
        <span>(+00) 000 000 000</span>
      </li>
      <li class="contact__item">
        <svg class="contact__icon" viewBox="0 0 12 12" aria-hidden="true"><path d="M3.5 0.5h5v11h-5Zm1 1v7.5h3V1.5ZM5.5 9.6h1v1h-1Z" fill-rule="evenodd"/></svg>
        <span>(+00) 000 000 000</span>
      </li>
      <li class="contact__item">
        <svg class="contact__icon" viewBox="0 0 12 12" aria-hidden="true"><path d="M0.5 2.5h11v1L6 7 0.5 3.5Zm0 2.2L6 8.2l5.5-3.5v4.8H0.5Z"/></svg>
        <span>mara@carelumen-mail.com</span>
      </li>
    </ul>

    <svg class="wave" viewBox="0 0 610 40" preserveAspectRatio="none" aria-hidden="true">
      <path d="M0 24 Q 300 19 610 6 L610 40 L0 40 Z" fill="var(--brand-blue)"/>
      <path d="M200 22 Q 420 14 610 2 L610 0 Q 420 10 200 21 Z" fill="var(--brand-green)"/>
      <path d="M120 22.5 Q 400 17 610 4.5" fill="none" stroke="var(--brand-green)" stroke-width="3"/>
    </svg>
  </section>

</body>
</html>
```